Therapeutic Counselling Practice Brochure

I have a new therapeutic counselling practice in Melbourne.

I am making peri natal issues my special interest area.

I need a brochure targeted at new parents or pregnant women and partners, struggling with the concept of parenting, depression, maybe do not even know about it.

The feel should be safe and strong. I love the KESTA website ( I do volunteer work with them)

Out of hours appointments and telephone counselling are important making my service very accessible.

Attached is an example for the content of the Brochure

Attached is an example for the content of the Brochure.

Target Market(s)

25 - 45 New Parents , expectant parents,families and friends of people struggling emotionally and mentally with and around being new parents

Requirements
Must have
• Feel of safety, somewhere to go for help, support, a conversation, soft ,strong
Nice to have
• mother and child, maybe parents and child, possibly a graphic, faceless

```html
<!DOCTYPE html>
<html lang="en">
<head>
<meta charset="utf-8">
<title>Perinatal Counselling Brochure</title>
<link rel="stylesheet" href="https://fonts.googleapis.com/css2?family=Arimo:wght@400;700&display=swap">
<style>
  :root {
    --bg: #b9ecc0;
    --green: #3f9e35;
    --green-dark: #2e7f27;
    --green-light: #5cb94c;
    --yellow: #f2e21a;
    --paper: #f4f6f2;
    --ink: #2c2c2c;
    --white: #ffffff;
  }
  * { box-sizing: border-box; margin: 0; padding: 0; }
  html, body { width: 1200px; height: 812px; overflow: hidden; }
  body {
    background: var(--bg);
    font-family: "Arimo", Arial, sans-serif;
    position: relative;
  }
  .brochure {
    position: absolute; left: 30px; top: 36px;
    width: 1140px; height: 740px;
    display: flex;
    box-shadow: 0 10px 30px rgba(0,60,0,.18);
  }
  .panel { position: relative; width: 380px; height: 740px; overflow: hidden; }

  /* Panel 1 */
  .panel--article { background: linear-gradient(180deg, #eef1ec, var(--paper)); }
  .article-header { position: absolute; left: 0; top: 0; width: 380px; height: 92px; }
  .article-title {
    position: absolute; left: 42px; top: 24px; width: 320px;
    color: var(--yellow); font-weight: 700; font-size: 15px; line-height: 18px;
    text-transform: uppercase;
  }
  .article-title::before {
    content: ""; position: absolute; left: -20px; top: 5px;
    border-left: 10px solid var(--yellow);
    border-top: 9px solid transparent; border-bottom: 9px solid transparent;
  }
  .article-body {
    position: absolute; left: 26px; top: 104px; width: 330px;
    color: var(--ink); font-size: 12.4px; line-height: 17px; text-align: justify;
  }
  .article-body p { margin-bottom: 10px; }
  .article-photo {
    position: absolute; left: 0; bottom: 0; width: 380px; height: 206px;
    background: linear-gradient(180deg, #e9a74a 0%, #c9772a 45%, #3a2a1c 100%);
    border-top-right-radius: 42px;
  }

  /* Panel 2 */
  .panel--contact {
    background: linear-gradient(180deg, var(--green-light), var(--green));
    color: var(--white); text-align: center;
  }
  .contact-photo {
    position: absolute; left: 22px; top: 26px; width: 336px; height: 234px;
    background: linear-gradient(135deg, #dce9c9, #9fbf7a 55%, #6e8f4a);
    border: 4px solid var(--yellow);
    border-radius: 36px 6px 36px 6px;
  }
  .contact-address { position: absolute; left: 0; top: 282px; width: 380px; font-weight: 700; font-size: 14px; line-height: 18px; }
  .contact-info { position: absolute; left: 40px; top: 372px; width: 300px; font-size: 12.4px; line-height: 17px; }
  .contact-info p { margin-bottom: 12px; }
  .contact-booking { position: absolute; left: 0; top: 560px; width: 380px; font-weight: 700; font-size: 14px; line-height: 19px; }

  /* Panel 3 */
  .panel--cover { background: var(--white); }
  .cover-top-band { position: absolute; left: 0; top: 0; width: 380px; height: 40px; }
  .cover-url { position: absolute; right: 26px; top: 12px; color: var(--yellow); font-size: 12px; font-weight: 700; }
  .brand-name {
    position: absolute; left: 0; top: 150px; width: 380px; text-align: center;
    color: var(--green); font-weight: 700; font-size: 26px;
  }
  .brand-name::before {
    content: ""; display: block; width: 90px; height: 90px; margin: 0 auto 18px;
    border-radius: 50%; background: var(--green);
  }
  .cover-heading {
    position: absolute; left: 0; top: 350px; width: 380px; text-align: center;
    color: var(--green-dark); font-weight: 700; font-size: 17px; line-height: 22px;
  }
  .cover-wave { position: absolute; left: 0; top: 400px; width: 380px; height: 340px; }
  .cover-message {
    position: absolute; left: 30px; top: 470px; width: 320px; text-align: center;
    color: var(--white); font-weight: 700; font-size: 13.5px; line-height: 19px;
  }
  .cover-signature {
    position: absolute; left: 0; top: 590px; width: 380px; text-align: center;
    color: var(--yellow); font-weight: 700; font-size: 14px; line-height: 18px;
  }
</style>
</head>
<body>
<main class="brochure">

  <section class="panel panel--article">
    <svg class="article-header" viewBox="0 0 380 92" aria-hidden="true">
      <path d="M0 0H380V62C300 62 260 80 190 80C120 80 60 72 0 80Z" fill="#3f9e35"/>
      <path d="M0 80C60 72 120 80 190 80C260 80 300 62 380 62V70C300 70 260 88 190 88C120 88 60 80 0 88Z" fill="#f2e21a"/>
    </svg>
    <h2 class="article-title">Depression in men after the birth of their baby</h2>
    <div class="article-body">
      <p>Becoming a father can be difficult to cope with and some men feel they have nowhere to turn for support. According to recent research, about <strong>10 per cent of new fathers</strong> become depressed after the birth of their child. www.parentwellbeing.org</p>
      <p>Having a new baby is a huge change, involving physical exhaustion and extra worries. It can be particularly difficult to balance the demands of work and fatherhood, especially as you might feel under pressure to earn more while your partner is not able to work.</p>
      <p>For new parents the focus of attention will have shifted and this can feel like a loss as well as a gain. Some men report feeling overwhelmed, isolated and confused by their feelings and their partner's reaction to them. They are often irritable, aggressive and sometimes hostile.</p>
      <p>Symptoms can include feeling very low - for example, not enjoying anything, poor concentration, perhaps a poor appetite and worrying at night. Some men feel ashamed of their feelings and experiences and this makes it very difficult for them to seek out and receive help.</p>
      <p>Counselling can help, being able to talk openly and honestly in a safe and confidential space.</p>
    </div>
    <div class="article-photo" role="img" aria-label="Photo: silhouette of a father holding his child by a lake at sunset"></div>
  </section>

  <section class="panel panel--contact">
    <div class="contact-photo" role="img" aria-label="Portrait photo of the counsellor among green leaves"></div>
    <p class="contact-address">Maren Holloway J.P.<br>Office: Level 2,<br>48 Linden Street,<br>Southbank 3006</p>
    <div class="contact-info">
      <p>Evening and weekend appointments available.<br>Telephone Counselling saves travel time and the hassle of parking. Telephone counselling gives you a convenient option in accessing therapy.</p>
      <p>Some people feel more comfortable discussing issues over the telephone, still within the safe supportive and confidential framework.</p>
      <p>Telephone appointments are usually available within 48 hours.</p>
    </div>
    <p class="contact-booking">To book please contact<br>Maren Holloway<br>on 0400 555 018<br>maren@marenholloway.com.au<br>www.marenholloway.com.au</p>
  </section>

  <section class="panel panel--cover">
    <svg class="cover-top-band" viewBox="0 0 380 40" aria-hidden="true">
      <path d="M0 0H380V34H0Z" fill="#3f9e35"/>
      <path d="M0 34H380V38H0Z" fill="#f2e21a"/>
    </svg>
    <span class="cover-url">marenholloway.com.au</span>
    <p class="brand-name">Maren Holloway</p>
    <h1 class="cover-heading">Are you Expecting or a New Parent?<br>Got the 'Baby Blues'?</h1>
    <svg class="cover-wave" viewBox="0 0 380 340" aria-hidden="true">
      <path d="M0 40C90 10 200 0 380 20V340H0Z" fill="#3f9e35"/>
    </svg>
    <p class="cover-message">There is an expectation of happiness and fulfilment around childbirth.<br>Feeling "blue", interferes with the adjustment to becoming a parent.<br>Sharing your feelings by talking is important.</p>
    <p class="cover-signature">Maren Holloway<br>Counsellor and Personal Coach</p>
  </section>

</main>
</body>
</html>
```